Data Compass Plan- Brennal Insurance providing specialist Cyber and Liability Insurance

for Managed Technology Service Providers and their customer, we will use a letterhead that white labels insurer documents, which can be used in our physical letters as well as to be used within Email signatures.

Target Market(s)

Managed Technology Services Providers

Industry/Entity Type

Cyber Insurance

Requirements
Must have
• website, email address, contact phone numbers

```html
<!DOCTYPE html>
<html lang="en">
<head>
<meta charset="utf-8">
<title>Data Compass Plan – Letterhead and Email Signature</title>
<link href="https://fonts.googleapis.com/css2?family=Arimo:wght@400;700&family=Mulish:wght@600;700&display=swap" rel="stylesheet">
<style>
  :root {
    --backdrop: #dfdfdf;
    --paper: #ffffff;
    --ink: #4a4a4c;
    --ink-soft: #5a5a5c;
    --brand-green: #39b54a;
    --rule: #6b6b6d;
  }
  * { box-sizing: border-box; margin: 0; padding: 0; }
  html, body {
    width: 1085px; height: 1200px; overflow: hidden;
    background: var(--backdrop);
    font-family: "Arimo", Arial, sans-serif;
    color: var(--ink);
  }
  .canvas { position: relative; width: 1085px; height: 1200px; }

  .sheet {
    position: absolute; background: var(--paper);
    box-shadow: 2px 2px 4px rgba(0,0,0,0.35);
  }

  /* Letterhead */
  .letterhead { left: 245px; top: 60px; width: 596px; height: 843px; }
  .wordmark {
    position: absolute; font-family: "Mulish", sans-serif; font-weight: 700;
    color: var(--ink); white-space: nowrap; letter-spacing: 0.5px;
  }
  .letterhead .wordmark { left: 39px; top: 50px; font-size: 24px; line-height: 30px; }
  .issuer {
    position: absolute; right: 41px; top: 45px; text-align: right;
    font-size: 9.3px; line-height: 12px; color: var(--ink);
  }
  .issuer .issuer-name { color: var(--brand-green); font-weight: 700; font-size: 9.6px; margin-bottom: 1px; }

  .salutation {
    position: absolute; left: 54px; top: 318px;
    font-family: "Mulish", sans-serif; font-weight: 700; font-size: 13.4px; color: var(--ink);
  }
  .letter-body { position: absolute; left: 53px; top: 358px; width: 492px; }
  .letter-body p {
    font-size: 9.6px; line-height: 12.2px; color: var(--ink-soft); margin-bottom: 11px;
  }
  .closing {
    position: absolute; left: 54px; top: 611px;
    font-family: "Mulish", sans-serif; font-weight: 700; font-size: 7.5px; color: var(--ink);
  }
  .signature-area {
    position: absolute; left: 52px; top: 645px; width: 92px; height: 27px;
    background: linear-gradient(90deg, #f1f1f1, #e6e6e6); border-radius: 3px;
  }
  .letter-footer {
    position: absolute; left: 58px; top: 807px; display: flex; align-items: center;
    font-size: 9.5px; color: var(--ink); white-space: nowrap;
  }
  .letter-footer .icon { width: 7px; height: 7px; margin-right: 6px; }
  .letter-footer .item { display: flex; align-items: center; margin-right: 9px; }
  .letter-footer .sep { margin: 0 7px 0 -2px; }

  /* Email signature */
  .signature-card { left: 245px; top: 941px; width: 596px; height: 202px; }
  .signature-card .wordmark { left: 30px; top: 24px; font-size: 33px; line-height: 42px; }
  .sig-issuer { position: absolute; left: 30px; top: 77px; }
  .sig-issuer .issuer-name {
    color: var(--brand-green); font-weight: 700; font-size: 15px; line-height: 18px;
  }
  .sig-issuer .reg { font-size: 15px; line-height: 18px; color: var(--ink); }
  .sig-issuer .reg:first-of-type { margin-top: 2px; }
  .sig-address {
    position: absolute; left: 30px; top: 144px; width: 477px;
    font-size: 15px; line-height: 18px; padding-bottom: 1px;
    border-bottom: 1px solid var(--rule);
  }
  .sig-contacts {
    position: absolute; left: 30px; top: 168px; display: flex; align-items: center;
    font-size: 15px; color: var(--ink); white-space: nowrap;
  }
  .sig-contacts .item { display: flex; align-items: center; margin-right: 13px; }
  .sig-contacts .icon { width: 11px; height: 11px; margin-right: 9px; }
</style>
</head>
<body>
<div class="canvas">

  <section class="sheet letterhead">
    <div class="wordmark">Data Compass Plan</div>
    <div class="issuer">
      <div class="issuer-name">Brennal Insurance</div>
      <div>ABN no: 48 203 915 662</div>
      <div>Corporate Authorised Representative no: 1340952</div>
    </div>

    <div class="salutation">Dear Mr. Smith,</div>
    <div class="letter-body">
      <p>Lorem ipsum dolor sit amet, consectetuer adipiscing elit, sed diam nonmmy nibh euismod tincidunt ut laor eet dolore magna aliquam erat volutpat. Ut wisi enim ad minim veniam, quis nostrud exerci tationmcorper suscipit lobortis nisl ut aliquip ex ea commodo consequat. Duis autem vel eum iriure dolor in hendrerit in vulputate velit esse molestie consequat, vel illum dolore eu feugiat</p>
      <p>Rorem ipsum dolor sit amet, consectetuer adipiscing elit, sed diam nonmmy nibh euismod tincidunt ut laor eet dolore magna aliquam erat volutpat. Ut wisi enim ad minim veniam, quis nostrud exerci tationmcorper suscipit lobortis nisl ut aliquip ex ea commodo consequat. Duis autem vel eum iriure dolor in hendrerit in vulputate velit esse molest</p>
      <p>Dorem ipsum dolor sit amet, consectetuer adipiscing elit, sed diam nonmmy nibh euismod tincidunt ut laor eet dolore magna aliquam erat volutpat. Ut wisi enim ad minim veniam, quis nostrud exerci tationmcorper suscipit lobortis nisl ut aliquip ex ea commodo consequat. Duis autem vel eum iriure dolor in hendrerit in suscipit lobortis nisl ut aliquip ex ea commodo consequat. Duis autem vel eum iriure dolor in hendrerit in vulputate velit esse molestie consequat, vel illum</p>
      <p>Sorem ipsum dolor sit amet, consectetuer adipiscing elit, sed diam nonmmy nibh euismod tincidunt ut laor eet dolore magna aliquam erat volutpat. Ut wisi enim ad minim veniam, quis nostrud exerci tationmcorper suscipit lobortis nisl ut aliquip ex ea commodo consequat. Duis autem vel eum iriure dolor in</p>
    </div>
    <div class="closing">Sincerely,</div>
    <div class="signature-area" role="img" aria-label="Handwritten signature of the sender"></div>

    <div class="letter-footer">
      <span class="item">
        <svg class="icon" viewBox="0 0 10 10"><path d="M2 0.5 L3.6 2.8 L2.6 3.8 Q3.6 6 6.2 7.4 L7.2 6.4 L9.5 8 L8.2 9.5 Q4.5 9.3 2 6.5 Q0.2 4 0.5 1.8 Z" fill="var(--brand-green)"/></svg>123-456-2100
      </span>
      <span class="item">
        <svg class="icon" viewBox="0 0 10 10"><rect x="0.5" y="2" width="9" height="6" fill="var(--brand-green)"/><path d="M0.5 2 L5 5.6 L9.5 2" fill="none" stroke="#fff" stroke-width="0.9"/></svg>youremail@mailbox.com
      </span>
      <span class="item">
        <svg class="icon" viewBox="0 0 10 10"><circle cx="5" cy="5" r="4.6" fill="var(--brand-green)"/><path d="M2.4 3 Q4 3.4 4.2 5 Q5.8 5.6 5 7.8 M6.4 1.6 Q6 3.2 7.8 3.8" fill="none" stroke="#fff" stroke-width="0.9"/></svg>www.yourwebsite.com
      </span>
      <span class="sep">|</span>
      <span>Your address, city, state, ZIP 0000</span>
    </div>
  </section>

  <section class="sheet signature-card">
    <div class="wordmark">Data Compass Plan</div>
    <div class="sig-issuer">
      <div class="issuer-name">by Brennal Insurance</div>
      <div class="reg">ABN no: 48 203 915 662</div>
      <div class="reg">Corporate Authorised Representative no: 1340952</div>
    </div>
    <div class="sig-address">Your address, city, state, ZIP 0000</div>
    <div class="sig-contacts">
      <span class="item">
        <svg class="icon" viewBox="0 0 10 10"><path d="M2 0.5 L3.6 2.8 L2.6 3.8 Q3.6 6 6.2 7.4 L7.2 6.4 L9.5 8 L8.2 9.5 Q4.5 9.3 2 6.5 Q0.2 4 0.5 1.8 Z" fill="var(--brand-green)"/></svg>123-456-2100
      </span>
      <span class="item">
        <svg class="icon" viewBox="0 0 10 10"><rect x="0.5" y="2" width="9" height="6" fill="var(--brand-green)"/><path d="M0.5 2 L5 5.6 L9.5 2" fill="none" stroke="#fff" stroke-width="0.9"/></svg>youremail@mailbox.com
      </span>
      <span class="item">
        <svg class="icon" viewBox="0 0 10 10"><circle cx="5" cy="5" r="4.6" fill="var(--brand-green)"/><path d="M2.4 3 Q4 3.4 4.2 5 Q5.8 5.6 5 7.8 M6.4 1.6 Q6 3.2 7.8 3.8" fill="none" stroke="#fff" stroke-width="0.9"/></svg>www.yourwebsite.com
      </span>
    </div>
  </section>

</div>
</body>
</html>
```